Cover für Podcast gesucht
Zielgruppe
Wir wollen einen PODCAST Rund um das Thema Business, Digitale Transformation und Tech starten. Unsere Zielgruppe sind Entscheidungsträger*innen die sich über aktuelle Trends, digitale und tech-orientierte Geschäftsmodelle sowie Tools und Management-Methoden auf dem Laufenden halten möchten.
Aufgabenstellung
ACHTUNG: ES HANDELT SICH HIERBEI UM EIN PODCAST COVER: Wir möchten auf dem Cover unsere beiden Fotos, die wir liefern, integriert haben sowie auch einen Schriftzug mit dem Namen 'wolkig verzweigt', der auch künftig als Logo für unsere Website fungieren soll. Das Cover soll das Thema 'digitalisierung', 'innovation', 'technologie / tech' 'trendy' umreißen.
Auf dem Cover sollten die beiden Bilder unserer Personen, der Schriftzug 'wolkig verzweigt' und darunter (subline) Business & Tech Talk stehen.

```html
<!DOCTYPE html>
<html lang="de">
<head>
<meta charset="utf-8">
<title>wolkig verzweigt – Podcast Cover</title>
<link rel="stylesheet" href="https://fonts.googleapis.com/css2?family=Raleway:wght@300;600;800&family=Poppins:wght@700&display=swap">
<style>
  :root {
    --sky: #5797d6;
    --sky-light: #6eaee4;
    --sky-deep: #4f8acb;
    --frame: #b8def0;
    --photo-dark: #3e6175;
    --photo-mid: #6f98ad;
    --photo-light: #a7cbdc;
    --band: #275a82;
    --white: #ffffff;
  }
  * { margin: 0; padding: 0; box-sizing: border-box; }
  html, body { width: 1200px; height: 1200px; overflow: hidden; background: var(--sky); }
  .cover { position: relative; width: 1200px; height: 1200px; overflow: hidden; background: var(--sky); }
  .backdrop, .hosts, .frame { position: absolute; inset: 0; width: 1200px; height: 1200px; }
  .title {
    position: absolute; left: 0; right: 0; text-align: center; color: var(--white);
    font-family: "Raleway", sans-serif; text-transform: uppercase; line-height: 1;
  }
  .title-main { top: 765px; font-weight: 800; font-size: 108px; letter-spacing: 1px; }
  .title-sub { top: 880px; font-weight: 300; font-size: 78px; letter-spacing: 2px; }
  .subline {
    position: absolute; left: 0; right: 0; top: 990px; text-align: center; color: var(--white);
    font-family: "Raleway", sans-serif; font-weight: 600; font-size: 36px; letter-spacing: 4px;
    text-transform: uppercase; line-height: 1;
  }
  .brand-mark {
    position: absolute; left: 0; right: 0; top: 505px; display: flex; flex-direction: column;
    align-items: center; gap: 10px; color: var(--white);
    font-family: "Raleway", sans-serif; font-weight: 800; font-size: 20px; letter-spacing: 1px;
  }
  .brand-dot { width: 86px; height: 86px; border: 7px solid var(--white); border-radius: 50%; }
  .host-band {
    position: absolute; left: 0; bottom: 0; width: 1200px; height: 104px; background: var(--band);
    font-family: "Poppins", sans-serif; font-weight: 700; color: var(--white);
  }
  .host-name { position: absolute; top: 50%; transform: translate(-50%, -50%); font-size: 41px; white-space: nowrap; letter-spacing: -0.5px; }
  .host-left { left: 285px; }
  .host-and { left: 600px; font-size: 60px; }
  .host-right { left: 925px; }
</style>
</head>
<body>
<div class="cover">
  <svg class="backdrop" viewBox="0 0 1200 1200" aria-hidden="true">
    <rect width="1200" height="1200" fill="var(--sky)"/>
    <path d="M335 0 C320 120 360 260 520 330 C700 410 900 380 1200 220 L1200 0 Z" fill="var(--sky-light)" opacity="0.45"/>
    <path d="M0 120 C160 80 330 110 520 210 C700 300 800 420 880 600 L0 600 Z" fill="var(--sky-light)" opacity="0.35"/>
    <path d="M0 500 C100 560 200 580 300 560 L0 700 Z" fill="var(--sky-deep)" opacity="0.4"/>
  </svg>
  <svg class="frame" viewBox="0 0 1200 1200" aria-hidden="true">
    <path d="M67 620 V67 H1133 V620" fill="none" stroke="var(--frame)" stroke-width="15"/>
  </svg>
  <svg class="hosts" viewBox="0 0 1200 1200">
    <g role="img" aria-label="Porträtfoto des ersten Hosts in blauer Tönung, kariertes Hemd">
      <path d="M0 665 C80 640 150 630 200 610 C180 560 170 480 175 430 C170 330 200 240 290 200 C380 175 470 200 510 280 C540 350 530 430 505 520 C500 560 520 580 560 610 C620 640 660 700 660 800 L660 1096 L0 1096 Z" fill="var(--photo-mid)"/>
      <path d="M175 430 C170 330 200 240 290 200 C380 175 470 200 510 280 C500 250 420 240 330 300 C250 330 220 400 175 430 Z" fill="var(--photo-dark)"/>
    </g>
    <g role="img" aria-label="Porträtfoto des zweiten Hosts in blauer Tönung, dunkle Steppjacke">
      <path d="M560 1096 C580 900 620 760 700 700 C760 670 790 640 760 590 C720 520 710 430 730 350 C760 260 860 200 960 220 C1050 240 1080 320 1080 400 C1090 470 1070 520 1060 570 C1130 560 1200 560 1200 560 L1200 1096 Z" fill="var(--photo-dark)"/>
      <path d="M770 380 C780 300 860 260 950 270 C1030 285 1060 350 1055 430 C1050 520 1000 590 920 600 C840 600 780 520 770 380 Z" fill="var(--photo-light)" opacity="0.55"/>
    </g>
  </svg>
  <div class="brand-mark"><span class="brand-dot"></span><span>wolkig verzweigt</span></div>
  <h1 class="title title-main">Wolkig</h1>
  <p class="title title-sub">Verzweigt</p>
  <p class="subline">Business &amp; Tech Talk</p>
  <div class="host-band">
    <span class="host-name host-left">Markus Lindner</span>
    <span class="host-name host-and">&amp;</span>
    <span class="host-name host-right">Jonas Brehm</span>
  </div>
</div>
</body>
</html>
```